Stationary for Tovin Consulting

Hi

I am after stationary designs for my company - Tovin Consulting. I have a logo - recently designed by ArtHarbor. Tovin ( nivot spelt backwards ) is a sales consultancy - including sales training, sales coaching and business management.

I have attached some of the artwork I already have, as well as a few ideas
1. Use supplied logo's
2. back of business card to use the logo with the dark background and white text
3. details to be included on card are
Logo
Delia Marquand
p: +61409827316
e: delia@tovinconsulting.com.au
w: www.tovinconsulting.com.au
PO Box 412, Kelby Heights, Victoria, 3187

4. I am after designs for business cards, A4 letterhead and A5 letterhead

Thanks in Advance

Delia

Industry/Entity Type

It Company

```html
<!DOCTYPE html>
<html lang="en">
<head>
<meta charset="UTF-8">
<title>Tovin Consulting – Business Card</title>
<link rel="stylesheet" href="https://fonts.googleapis.com/css2?family=Montserrat:wght@600&family=Questrial&display=swap">
<style>
  :root {
    --slate: #34444f;
    --slate-deep: #222d35;
    --cream-light: #fdf3b8;
    --cream-warm: #f8cd93;
    --accent: #d9492a;
    --white: #ffffff;
    --page: #ffffff;
  }
  * { margin: 0; padding: 0; box-sizing: border-box; }
  html, body { width: 1200px; height: 900px; overflow: hidden; background: var(--page); }
  .canvas { position: relative; width: 1200px; height: 900px; }

  .card { position: absolute; overflow: hidden; }
  .card svg.card-art { position: absolute; inset: 0; width: 100%; height: 100%; }

  .card-front { left: 26px; top: 285px; width: 550px; height: 337px; }
  .card-back { left: 611px; top: 290px; width: 549px; height: 338px; background: var(--slate); }

  .brand-name {
    position: absolute;
    font-family: "Montserrat", sans-serif;
    font-weight: 600;
    white-space: nowrap;
    letter-spacing: 0.5px;
  }
  .card-front .brand-name { left: 108px; top: 140px; font-size: 34px; color: var(--slate); }
  .card-back .brand-name { right: 28px; top: 44px; font-size: 22px; color: var(--white); }

  .holder-name {
    position: absolute;
    right: 40px; top: 168px;
    font-family: "Questrial", sans-serif;
    font-size: 22px;
    color: var(--white);
  }
  .holder-rule {
    position: absolute;
    left: 402px; right: 0; top: 194px;
    height: 2px; background: var(--accent);
  }

  .contact-list {
    position: absolute;
    left: 142px; top: 246px;
    list-style: none;
    font-family: "Questrial", sans-serif;
    font-size: 13px;
    color: var(--white);
    line-height: 17.5px;
  }
  .contact-list li { display: flex; align-items: center; gap: 8px; }
  .contact-list svg { width: 12px; height: 12px; flex: none; }
  .contact-list .web { color: var(--accent); }
</style>
</head>
<body>
<div class="canvas">

  <section class="card card-front">
    <svg class="card-art" viewBox="0 0 550 337" aria-hidden="true">
      <defs>
        <radialGradient id="frontGlow" cx="48%" cy="52%" r="70%">
          <stop offset="0" stop-color="var(--cream-light)"/>
          <stop offset="1" stop-color="var(--cream-warm)"/>
        </radialGradient>
        <linearGradient id="frontBand" x1="0" y1="0" x2="1" y2="0">
          <stop offset="0" stop-color="var(--slate)"/>
          <stop offset="1" stop-color="var(--slate-deep)"/>
        </linearGradient>
      </defs>
      <rect width="550" height="337" fill="url(#frontGlow)"/>
      <polygon points="420,0 448,0 550,103 550,225 417,93" fill="url(#frontBand)"/>
      <polygon points="337,326 504,173 550,215 550,247 460,337 337,337" fill="var(--slate)"/>
      <rect x="0" y="326" width="550" height="11" fill="var(--accent)"/>
    </svg>
    <div class="brand-name">Tovin Consulting</div>
  </section>

  <section class="card card-back">
    <svg class="card-art" viewBox="0 0 549 338" aria-hidden="true">
      <defs>
        <linearGradient id="backBand" x1="0" y1="0" x2="1" y2="0">
          <stop offset="0" stop-color="var(--cream-light)"/>
          <stop offset="1" stop-color="var(--cream-warm)"/>
        </linearGradient>
      </defs>
      <polygon points="89,0 213,0 50,156 0,112 0,88" fill="url(#backBand)"/>
      <polygon points="0,114 119,220 129,338 101,338 0,235" fill="url(#backBand)"/>
    </svg>
    <div class="brand-name">Tovin Consulting</div>
    <div class="holder-name">Delia Marquand</div>
    <div class="holder-rule"></div>
    <ul class="contact-list">
      <li>
        <svg viewBox="0 0 12 12"><path d="M2 1h2l1 3-1.5 1a6 6 0 0 0 3 3L7.5 6.5l3 1v2a1.5 1.5 0 0 1-1.5 1.5A8 8 0 0 1 1 2.5 1.5 1.5 0 0 1 2 1z" fill="var(--accent)"/></svg>
        +61409827316
      </li>
      <li>
        <svg viewBox="0 0 12 12"><rect x="0.5" y="2.5" width="11" height="7" fill="none" stroke="var(--accent)"/><path d="M0.5 2.5 6 7l5.5-4.5" fill="none" stroke="var(--accent)"/></svg>
        delia@tovinconsulting.com.au
      </li>
      <li class="web">
        <svg viewBox="0 0 12 12"><circle cx="6" cy="6" r="4" fill="var(--accent)"/></svg>
        www.tovinconsulting.com.au
      </li>
      <li>
        <svg viewBox="0 0 12 12"><path d="M6 0.5a4 4 0 0 1 4 4c0 3-4 7-4 7s-4-4-4-7a4 4 0 0 1 4-4z" fill="var(--accent)"/><circle cx="6" cy="4.5" r="1.4" fill="var(--slate)"/></svg>
        PO Box 412, Kelby Heights, Victoria, 3187
      </li>
    </ul>
  </section>

</div>
</body>
</html>
```